Swimming Pool Supply Company Business Cards

We need business cards designed for company. These need to be easy to edit so that we can fill in names, titles, and contact info for each person who works here.

Dalton R. Whitfield
Manager of Legal & Finance
K.L. Brisbane, Incorporated

4837 Grenway Avenue
Marlow Heights, PA 19243

E. dalton@klbrisbane-example.com
M. (215) 555-0173
O. (215) 555-0148

Contact Information for Business Card

Looking to upgrade current business cards with graphic that can be edited. Looking for fresh ideas for an age old industry.

Font styles to use
Serif
Sans Serif

Colors

Designer to choose colors to be used in the design.

Requirements
Must have
• Professional, fresh, unique but professional

```html
<!DOCTYPE html>
<html lang="en">
<head>
<meta charset="utf-8">
<title>K.L. Brisbane, Incorporated — Business Card</title>
<link rel="stylesheet" href="https://fonts.googleapis.com/css2?family=Roboto+Condensed:wght@700&family=Roboto:wght@400;700&family=Open+Sans:wght@400&display=swap">
<style>
  :root {
    --backdrop: #e9e6e1;
    --card-front: #f7f7f7;
    --card-back: #252324;
    --ink-dark: #1e1e1e;
    --ink-muted: #8e8e8e;
    --ink-body: #4a4a4a;
    --rule: #6a6a6a;
    --ink-light: #f2f2f2;
  }
  * { margin: 0; padding: 0; box-sizing: border-box; }
  html, body {
    width: 1200px;
    height: 960px;
    overflow: hidden;
    background: var(--backdrop);
  }
  .canvas {
    position: relative;
    width: 1200px;
    height: 960px;
  }
  .card {
    position: absolute;
    width: 600px;
    height: 340px;
    border-radius: 22px;
  }
  .card--front {
    left: 302px;
    top: 135px;
    background: var(--card-front);
  }
  .card--back {
    left: 300px;
    top: 505px;
    background: var(--card-back);
  }
  .identity {
    position: absolute;
    top: 128px;
    left: 0;
    width: 100%;
    text-align: center;
  }
  .identity__name {
    font-family: "Roboto Condensed", "Arial Narrow", sans-serif;
    font-weight: 700;
    font-size: 27px;
    letter-spacing: 0.3px;
    color: var(--ink-dark);
    text-transform: uppercase;
    line-height: 32px;
  }
  .identity__title,
  .identity__company {
    font-family: "Roboto", Arial, sans-serif;
    font-size: 14.5px;
    color: var(--ink-muted);
    text-transform: uppercase;
    letter-spacing: 0.4px;
    line-height: 19px;
  }
  .contact {
    position: absolute;
    top: 264px;
    left: 70px;
    width: 462px;
    text-align: center;
    font-family: "Roboto", Arial, sans-serif;
    font-size: 14px;
    color: var(--ink-body);
    text-transform: uppercase;
    letter-spacing: 0.2px;
  }
  .contact__address {
    padding-bottom: 2px;
    border-bottom: 1px solid var(--rule);
    line-height: 18px;
  }
  .contact__lines {
    margin-top: 3px;
    white-space: nowrap;
    line-height: 18px;
    margin-left: -20px;
    margin-right: -20px;
  }
  .contact__item { margin: 0 4px; }
  .contact__label { font-weight: 700; color: var(--ink-dark); }
  .brand {
    position: absolute;
    top: 108px;
    left: 0;
    width: 100%;
    text-align: center;
    color: var(--ink-light);
  }
  .brand__name {
    font-family: "Roboto Condensed", "Arial Narrow", sans-serif;
    font-weight: 700;
    font-size: 74px;
    line-height: 80px;
    letter-spacing: 2px;
    text-transform: uppercase;
  }
  .brand__tagline {
    font-family: "Open Sans", Arial, sans-serif;
    font-size: 15.5px;
    line-height: 22px;
    margin-top: 0;
  }
</style>
</head>
<body>
  <main class="canvas">
    <section class="card card--front" aria-label="Business card front">
      <div class="identity">
        <h1 class="identity__name">Dalton R. Whitfield</h1>
        <p class="identity__title">Manager of Legal &amp; Finance</p>
        <p class="identity__company">K.L. Brisbane, Incorporated</p>
      </div>
      <div class="contact">
        <p class="contact__address">4837 Grenway Avenue, Marlow Heights, PA 19243</p>
        <p class="contact__lines">
          <span class="contact__item"><span class="contact__label">C</span> (215) 555-0173</span>
          <span class="contact__item"><span class="contact__label">O</span> (215) 555-0148</span>
          <span class="contact__item"><span class="contact__label">E</span> dalton@klbrisbane-example.com</span>
        </p>
      </div>
    </section>

    <section class="card card--back" aria-label="Business card back">
      <div class="brand">
        <p class="brand__name">Brisbane</p>
        <p class="brand__tagline">Big Enough to Serve You, Small Enough to Care</p>
      </div>
    </section>
  </main>
</body>
</html>
```